Halvery Metal Recyclers - www.halveryrecyclers.com.au

I've just rebranded my business and thought what better way to continue with this than getting a website.
It is going to be fairly basic for now. I've attached quite a few images, feel free to use whichever you like.
And pages description is also attached in a .doc file.
Updates

Hi, this is my first time having a website. I am open to anything and trust the experience and ideas you can bring forward. I will look at extending the deadline so I can take my time to give feedback as needed! Thank you all.

Target Market(s)

Mining and industrial and commercial sectors

Coding

Coded - Design and coding required

Number of Pages Required

5+ page

Requirements
Must have
• Logo/Phone number at the top of every page. "Scrap Metal Specialists" tag line at the top of every page.
Nice to have
• Top Navigation.

```html
<!DOCTYPE html>
<html lang="en">
<head>
<meta charset="utf-8">
<title>Halvery Metal Recyclers – Scrap Metal Specialists</title>
<link rel="stylesheet" href="https://fonts.googleapis.com/css2?family=Teko:wght@400;500&family=Poppins:wght@400;500;600&display=swap">
<style>
:root{
  --navy:#1f3a6e;
  --ink:#0d1a33;
  --gray:#8b8c91;
  --gray-dark:#6f7075;
  --light:#f4f4f4;
  --white:#ffffff;
  --text:#5a5a5a;
  --heading-font:"Teko",sans-serif;
  --body-font:"Poppins",sans-serif;
}
*{margin:0;padding:0;box-sizing:border-box}
html,body{width:1200px;height:3532px;overflow:hidden;background:var(--white)}
body{font-family:var(--body-font);color:var(--text)}
.page{position:relative;width:1200px;height:3532px;overflow:hidden}
.abs{position:absolute}
.backdrop{position:absolute;left:0;top:0}

/* header */
.hero-photo{left:0;top:0;width:1200px;height:722px;background:
  radial-gradient(ellipse at 78% 45%,#9a7a2c 0%,#5e4a1e 35%,transparent 70%),
  linear-gradient(100deg,#1d1e22 0%,#3d3522 40%,#5a4a22 65%,#2d2a22 100%)}
.top-bar{left:0;top:0;width:1200px;height:80px;background:rgba(12,24,48,.82)}
.brand{left:88px;top:0;width:225px;height:134px;background:var(--white);box-shadow:0 2px 6px rgba(0,0,0,.35);display:flex;flex-direction:column;align-items:center;justify-content:center;font-family:var(--heading-font);font-weight:500;color:var(--navy);line-height:.85;text-align:center}
.brand .brand-name{font-size:48px;letter-spacing:1px}
.brand .brand-sub{font-size:26px;letter-spacing:.5px}
.brand .brand-phone{font-size:22px;letter-spacing:1px;color:var(--navy)}
.main-nav{left:409px;top:27px;display:flex;gap:34px;align-items:center}
.main-nav a{font-family:var(--heading-font);font-size:17px;letter-spacing:1.2px;color:var(--white);text-decoration:none;text-transform:uppercase;line-height:30px}
.main-nav a.current{background:var(--gray);padding:0 20px;margin-right:-8px}
.call{left:993px;top:20px;display:flex;align-items:center;gap:8px;color:var(--white);font-family:var(--heading-font)}
.call .call-label{font-size:13px;letter-spacing:1px;color:#c9ccd3;line-height:1}
.call .call-number{font-size:19px;letter-spacing:.8px;line-height:1}
.hero-title{left:0;top:308px;width:1200px;text-align:center;font-family:var(--heading-font);font-weight:500;font-size:64px;letter-spacing:2px;color:var(--white);line-height:1;text-shadow:0 2px 6px rgba(0,0,0,.5)}
.btn{display:flex;align-items:center;justify-content:center;font-family:var(--heading-font);font-size:16px;letter-spacing:2px;color:var(--white);text-transform:uppercase;text-decoration:none}
.btn-dark{background:var(--ink)}
.btn-navy{background:var(--navy)}
.btn-gray{background:var(--gray)}
.hero-cta{left:529px;top:399px;width:141px;height:37px}
.badge-circle{width:80px;height:80px;border-radius:50%;background:var(--gray);border:4px solid rgba(255,255,255,.35)}

/* section headings */
.kicker{left:0;width:1200px;text-align:center;font-family:var(--heading-font);font-size:20px;letter-spacing:1px;color:var(--gray-dark);text-transform:uppercase}
.section-title{left:0;width:1200px;text-align:center;font-family:var(--heading-font);font-weight:500;font-size:40px;letter-spacing:1px;color:var(--navy);line-height:1;text-transform:uppercase}
.title-rule{height:3px;background:var(--gray-dark);width:60px;left:570px}

.welcome-text{left:168px;top:856px;width:864px;text-align:center;font-size:13.5px;line-height:19px;color:var(--text)}
.welcome-text p+p{margin-top:20px}
.about-cta{left:525px;top:1008px;width:151px;height:38px}

/* services */
.service-card{width:240px;height:309px;background:var(--white);padding:15px}
.service-card.active{background:var(--navy)}
.service-card .service-photo{width:210px;height:221px}
.service-card .service-name{position:absolute;left:15px;top:248px;width:160px;font-size:14.5px;font-weight:500;line-height:20px;color:var(--navy);height:42px;display:flex;align-items:center}
.service-card.active .service-name{color:var(--white)}
.arrow-btn{position:absolute;right:16px;top:250px;width:38px;height:38px;border-radius:50%;border:1.5px solid #777;display:flex;align-items:center;justify-content:center}
.service-card.active .arrow-btn{background:var(--gray);border-color:var(--gray)}

/* blogs */
.blog-photo{width:303px;height:212px}
.blog-box{width:279px;height:152px;background:var(--white);box-shadow:0 2px 12px rgba(0,0,0,.12);padding:22px 16px 0 16px;display:flex;gap:14px}
.blog-date{width:50px;text-align:center;flex-shrink:0}
.blog-date .day{font-size:30px;font-weight:600;color:var(--navy);line-height:1}
.blog-date .month{font-size:11px;color:var(--gray-dark);margin-top:4px}
.blog-body{font-size:15px;line-height:21px;color:#222}
.blog-body a{display:inline-block;margin-top:12px;font-size:13px;color:var(--navy);text-decoration:underline}
.view-all{left:544px;top:2544px;width:111px;height:39px}

/* inquiry */
.field-label{font-size:13px;color:var(--navy)}
.field{background:var(--white);border:1px solid #d3d3d3;width:272px;height:37px;display:flex;align-items:center;padding-left:12px}
.field.message{height:118px;align-items:flex-start;padding-top:12px}
.submit{left:552px;top:3002px;width:95px;height:39px}

/* footer */
.footer-brand{left:88px;top:3266px;width:200px;font-family:var(--heading-font);font-weight:500;color:#9aa5bd;text-align:center;line-height:.85}
.footer-brand .brand-name{font-size:50px;letter-spacing:1px}
.footer-brand .brand-sub{font-size:27px}
.footer-brand .brand-phone{font-size:23px;letter-spacing:1px}
.footer-heading{font-family:var(--heading-font);font-size:24px;letter-spacing:1px;color:var(--gray);text-transform:uppercase;line-height:1}
.contact-list{left:348px;top:3300px;list-style:none;color:var(--white);font-size:14.5px;line-height:20px}
.contact-list li{display:flex;gap:12px;margin-bottom:12px}
.contact-list svg{flex-shrink:0;margin-top:3px}
.quick-links{left:671px;top:3300px;list-style:none}
.quick-links a{display:block;color:var(--white);font-size:14.5px;line-height:24.6px;text-decoration:none}
.quick-links a.current{color:#9aa5bd;text-decoration:underline}
.footer-map{left:864px;top:3257px;width:247px;height:153px;background:linear-gradient(135deg,#dfe6d6,#c9d7bc 50%,#e7e0cc);border:2px solid #fff}
.bottom-bar{left:0;top:3492px;width:1200px;height:40px;background:var(--gray)}
.copyright{left:88px;top:3503px;font-size:13px;color:var(--white)}
.social{top:3500px;width:26px;height:26px;border-radius:50%;background:var(--white)}
.social.active{background:var(--navy)}
</style>
</head>
<body>
<div class="page">

  <!-- background shapes -->
  <div class="abs hero-photo" role="img" aria-label="Scrap metal yard at dusk with yellow machinery and a large wire cable drum"></div>
  <svg class="backdrop" width="1200" height="3532" viewBox="0 0 1200 3532" aria-hidden="true">
    <!-- hero to welcome -->
    <path d="M0,716 Q600,574 1200,716" fill="none" stroke="#8b8c91" stroke-width="7"/>
    <path d="M0,722 Q600,584 1200,722 L1200,1070 L0,1070 Z" fill="#ffffff"/>
    <!-- services band -->
    <rect x="0" y="1062" width="1200" height="1040" fill="#8b8c91"/>
    <path d="M0,1060 L1200,1060 L1200,1062 Q600,1214 0,1062 Z" fill="#ffffff"/>
    <path d="M250,1105 Q600,1160 950,1105" fill="none" stroke="#5f6065" stroke-width="2"/>
    <path d="M300,1118 Q600,1170 900,1118" fill="none" stroke="#ffffff" stroke-width="2.5"/>
    <path d="M0,2091 Q600,1939 1200,2091 L1200,2600 L0,2600 Z" fill="#ffffff"/>
    <path d="M300,2027 Q600,1990 900,2027" fill="none" stroke="#ffffff" stroke-width="2.5"/>
    <path d="M340,2038 Q600,2005 860,2038" fill="none" stroke="#5f6065" stroke-width="2"/>
    <!-- inquiry band -->
    <rect x="0" y="2591" width="1200" height="510" fill="#f4f4f4"/>
    <path d="M0,2589 L1200,2589 L1200,2591 Q600,2729 0,2591 Z" fill="#ffffff"/>
    <path d="M295,2636 Q600,2690 865,2636" fill="none" stroke="#5f6065" stroke-width="4"/>
    <!-- footer -->
    <rect x="0" y="3089" width="1200" height="403" fill="#1f3a6e"/>
    <path d="M0,3087 L1200,3087 L1200,3089 Q600,3217 0,3089 Z" fill="#f4f4f4"/>
    <path d="M0,3112 Q600,3228 1200,3112" fill="none" stroke="#8b8c91" stroke-width="6"/>
  </svg>

  <!-- header -->
  <div class="abs top-bar"></div>
  <div class="abs brand">
    <span class="brand-name">HALVERY</span>
    <span class="brand-sub">METAL RECYCLERS</span>
    <span class="brand-phone">0412558037</span>
  </div>
  <nav class="abs main-nav">
    <a class="current" href="#">Home</a>
    <a href="#">About Us</a>
    <a href="#">Services</a>
    <a href="#">Online Store</a>
    <a href="#">Blog</a>
    <a href="#">Contact Us</a>
  </nav>
  <div class="abs call">
    <svg width="24" height="24" viewBox="0 0 24 24" fill="none" stroke="#c9ccd3" stroke-width="1.4"><circle cx="12" cy="12" r="11"/><path d="M8 6.5l2 2.5-1.2 1.4a7 7 0 0 0 4.8 4.8L15 14l2.5 2-1.3 1.6C11 17 7 13 6.4 7.8z"/></svg>
    <div><div class="call-label">CALL</div><div class="call-number">0412558037</div></div>
  </div>
  <h1 class="abs hero-title">SCRAP METAL SPECIALISTS</h1>
  <a class="abs btn btn-dark hero-cta" href="#">Consult Now!</a>
  <div class="abs badge-circle" style="left:560px;top:607px"></div>

  <!-- welcome -->
  <p class="abs kicker" style="top:762px">Welcome to the website of</p>
  <h2 class="abs section-title" style="top:788px;font-size:38px">Halvery Metal Recyclers.</h2>
  <div class="abs title-rule" style="top:827px"></div>
  <div class="abs welcome-text">
    <p>We are a Perth based company that provides scrap metal collection and oxy cutting services in the mining, construction, and industrial sectors all around WA.</p>
    <p>My name is Sam Halvery and I'm the managing director of Halvery Metal Processors. I have been in the scrap metal recycling industry longer than I haven't! I have 16 years' experience in everything scrap metal and I am very passionate about sustainable recycling</p>
  </div>
  <a class="abs btn btn-gray about-cta" href="#">More About Us</a>

  <!-- services -->
  <h2 class="abs section-title" style="top:1218px">Our Services</h2>
  <div class="abs title-rule" style="top:1255px;background:var(--navy)"></div>

  <div class="abs service-card" style="left:121px;top:1301px">
    <div class="service-photo" role="img" aria-label="Worker oxy cutting steel with sparks flying" style="background:linear-gradient(135deg,#5a4a3a,#8a5a30 55%,#2d2620)"></div>
    <div class="service-name">Oxy cutting and breaking down of</div>
    <div class="arrow-btn"><svg width="14" height="10" viewBox="0 0 14 10" fill="none" stroke="#333" stroke-width="1.4"><path d="M1 5h12M9 1l4 4-4 4"/></svg></div>
  </div>
  <div class="abs service-card active" style="left:361px;top:1301px">
    <div class="service-photo" role="img" aria-label="Heavy industrial plasma cutting machine in a blue-lit workshop" style="background:linear-gradient(135deg,#1c2f8a,#4a3fc2 55%,#121a40)"></div>
    <div class="service-name">Heavy industrial equipment</div>
    <div class="arrow-btn"><svg width="14" height="10" viewBox="0 0 14 10" fill="none" stroke="#fff" stroke-width="1.4"><path d="M1 5h12M9 1l4 4-4 4"/></svg></div>
  </div>
  <div class="abs service-card" style="left:601px;top:1301px">
    <div class="service-photo" role="img" aria-label="Steel mill rail rolling line with glowing metal" style="background:radial-gradient(circle at 55% 60%,#d06a20,#4a3a30 40%,#2a2a2a)"></div>
    <div class="service-name">Rail</div>
    <div class="arrow-btn"><svg width="14" height="10" viewBox="0 0 14 10" fill="none" stroke="#333" stroke-width="1.4"><path d="M1 5h12M9 1l4 4-4 4"/></svg></div>
  </div>
  <div class="abs service-card" style="left:841px;top:1301px">
    <div class="service-photo" role="img" aria-label="Laser cutter head throwing sparks over a steel plate" style="background:radial-gradient(circle at 50% 55%,#e8c070,#3a4a6a 35%,#1a2438)"></div>
    <div class="service-name">Mine site clean ups and demolition</div>
    <div class="arrow-btn"><svg width="14" height="10" viewBox="0 0 14 10" fill="none" stroke="#333" stroke-width="1.4"><path d="M1 5h12M9 1l4 4-4 4"/></svg></div>
  </div>

  <div class="abs service-card" style="left:121px;top:1627px">
    <div class="service-photo" role="img" aria-label="Worker in hard hat cutting a curved steel structure" style="background:linear-gradient(135deg,#6a6a6a,#c08040 50%,#2a4a7a)"></div>
    <div class="service-name">EWP and high risk work</div>
    <div class="arrow-btn"><svg width="14" height="10" viewBox="0 0 14 10" fill="none" stroke="#333" stroke-width="1.4"><path d="M1 5h12M9 1l4 4-4 4"/></svg></div>
  </div>
  <div class="abs service-card" style="left:361px;top:1627px">
    <div class="service-photo" role="img" aria-label="Scrap metal plates lying on the ground by a corrugated structure" style="background:linear-gradient(180deg,#6e6e70,#54504a 45%,#7a6a58)"></div>
    <div class="service-name">Scrap metal clean up and removal</div>
    <div class="arrow-btn"><svg width="14" height="10" viewBox="0 0 14 10" fill="none" stroke="#333" stroke-width="1.4"><path d="M1 5h12M9 1l4 4-4 4"/></svg></div>
  </div>
  <div class="abs service-card" style="left:601px;top:1627px">
    <div class="service-photo" role="img" aria-label="Rusty old gears and cogs" style="background:radial-gradient(circle at 40% 50%,#7a5a40,#3a302a 60%,#1e1a18)"></div>
    <div class="service-name">Transport and collection</div>
    <div class="arrow-btn"><svg width="14" height="10" viewBox="0 0 14 10" fill="none" stroke="#333" stroke-width="1.4"><path d="M1 5h12M9 1l4 4-4 4"/></svg></div>
  </div>
  <div class="abs service-card" style="left:841px;top:1627px">
    <div class="service-photo" role="img" aria-label="Scrap yard with yellow machinery and a large cable drum" style="background:linear-gradient(135deg,#4a4a4a,#8a7030 55%,#2a2620)"></div>
    <div class="service-name">Buyer of all types of scrap metal</div>
    <div class="arrow-btn"><svg width="14" height="10" viewBox="0 0 14 10" fill="none" stroke="#333" stroke-width="1.4"><path d="M1 5h12M9 1l4 4-4 4"/></svg></div>
  </div>

  <!-- blogs -->
  <h2 class="abs section-title" style="top:2102px">Our Blogs</h2>
  <div class="abs title-rule" style="top:2139px;background:var(--navy)"></div>

  <div class="abs blog-photo" style="left:121px;top:2184px" role="img" aria-label="Laser cutter sparks over steel plate" ></div>
  <div class="abs blog-photo" style="left:121px;top:2184px;background:radial-gradient(circle at 50% 55%,#e8c070,#3a4a6a 35%,#1a2438)"></div>
  <div class="abs blog-box" style="left:132px;top:2351px">
    <div class="blog-date"><div class="day">01</div><div class="month">Nov, 22</div></div>
    <div class="blog-body">Lorem Ipsum is simply dummy text of the printing and typesetting industry.<br><a href="#">Explore More</a></div>
  </div>

  <div class="abs blog-photo" style="left:448px;top:2184px;background:linear-gradient(135deg,#5a4a3a,#8a5a30 55%,#2d2620)" role="img" aria-label="Worker oxy cutting steel with sparks"></div>
  <div class="abs blog-box" style="left:459px;top:2351px">
    <div class="blog-date"><div class="day">13</div><div class="month">Nov, 22</div></div>
    <div class="blog-body">Lorem Ipsum is simply dummy text of the printing and typesetting industry.<br><a href="#">Explore More</a></div>
  </div>

  <div class="abs blog-photo" style="left:776px;top:2184px;background:linear-gradient(135deg,#8a8a8a,#c08040 50%,#2a4a7a)" role="img" aria-label="Worker cutting a curved steel structure"></div>
  <div class="abs blog-box" style="left:788px;top:2320px">
    <div class="blog-date"><div class="day">18</div><div class="month">Nov, 22</div></div>
    <div class="blog-body">Lorem Ipsum is simply dummy text of the printing and typesetting industry.<br><a href="#">Explore More</a></div>
  </div>

  <a class="abs btn btn-dark view-all" href="#">View All</a>

  <!-- quick inquiry -->
  <h2 class="abs section-title" style="top:2741px">Quick Inquiry</h2>
  <div class="abs title-rule" style="top:2778px;background:var(--navy)"></div>

  <label class="abs field-label" style="left:167px;top:2820px">First Name</label>
  <div class="abs field" style="left:167px;top:2843px"><svg width="12" height="12" viewBox="0 0 12 12" fill="none" stroke="#999"><circle cx="6" cy="4" r="2.5"/><path d="M1.5 11.5a4.5 4.5 0 0 1 9 0z"/></svg></div>
  <label class="abs field-label" style="left:463px;top:2820px">Last Name</label>
  <div class="abs field" style="left:463px;top:2843px"><svg width="12" height="12" viewBox="0 0 12 12" fill="none" stroke="#999"><circle cx="6" cy="4" r="2.5"/><path d="M1.5 11.5a4.5 4.5 0 0 1 9 0z"/></svg></div>
  <label class="abs field-label" style="left:760px;top:2820px">Your Message</label>
  <div class="abs field message" style="left:760px;top:2843px"><svg width="12" height="12" viewBox="0 0 12 12" fill="none" stroke="#999"><path d="M1 1h10v7l-3 3H1z"/></svg></div>
  <label class="abs field-label" style="left:167px;top:2901px">Phone Number</label>
  <div class="abs field" style="left:167px;top:2924px"><svg width="10" height="13" viewBox="0 0 10 13" fill="none" stroke="#999"><rect x="1" y="1" width="8" height="11" rx="1"/></svg></div>
  <label class="abs field-label" style="left:463px;top:2901px">Your Email</label>
  <div class="abs field" style="left:463px;top:2924px"><svg width="13" height="10" viewBox="0 0 13 10" fill="none" stroke="#999"><rect x="1" y="1" width="11" height="8"/><path d="M1 1l5.5 4L12 1"/></svg></div>
  <a class="abs btn btn-dark submit" href="#">Submit</a>

  <!-- footer -->
  <div class="abs badge-circle" style="left:560px;top:3122px"></div>
  <div class="abs footer-brand">
    <div class="brand-name">HALVERY</div>
    <div class="brand-sub">METAL RECYCLERS</div>
    <div class="brand-phone">0412558037</div>
  </div>
  <h3 class="abs footer-heading" style="left:348px;top:3264px">Conatct Info</h3>
  <ul class="abs contact-list">
    <li><svg width="14" height="18" viewBox="0 0 14 18" fill="#9aa5bd"><path d="M7 0a7 7 0 0 0-7 7c0 5 7 11 7 11s7-6 7-11a7 7 0 0 0-7-7zm0 10a3 3 0 1 1 0-6 3 3 0 0 1 0 6z"/></svg><span>14 Forge Rd, Welshpool,<br>WA 6106</span></li>
    <li><svg width="14" height="14" viewBox="0 0 14 14" fill="#9aa5bd"><path d="M3 0l2.5 3.5-1.5 1.8a8 8 0 0 0 4.7 4.7l1.8-1.5L14 11l-1.5 2.5C6 13 1 8 .5 1.5z"/></svg><span>0412558037</span></li>
    <li><svg width="15" height="11" viewBox="0 0 15 11" fill="none" stroke="#9aa5bd" stroke-width="1.3"><rect x="1" y="1" width="13" height="9"/><path d="M1 1l6.5 5L14 1"/></svg><span>sam@halveryrecyclers.com.au</span></li>
  </ul>
  <h3 class="abs footer-heading" style="left:671px;top:3264px">Quick Link</h3>
  <nav class="abs quick-links">
    <a class="current" href="#">Home</a>
    <a href="#">About Us</a>
    <a href="#">Our Services</a>
    <a href="#">Online Store</a>
    <a href="#">Our Blog</a>
    <a href="#">Contact Us</a>
  </nav>
  <div class="abs footer-map" role="img" aria-label="Location map of the business premises"></div>

  <div class="abs bottom-bar"></div>
  <p class="abs copyright">© 2022 Halvery Metal Recyclers. All Right Reserved</p>
  <span class="abs social" style="left:984px"></span>
  <span class="abs social active" style="left:1017px"></span>
  <span class="abs social" style="left:1051px"></span>
  <span class="abs social" style="left:1085px"></span>

</div>
</body>
</html>
```